2026 Varnel Kestra LWB Vehicle Wrap Design for RT Electrical and Refrigeration Work Vans

We are RT Electrical and Refrigeration — a Perth-based commercial electrical, air conditioning and refrigeration company. We service commercial buildings, homes and luxury residential jobs across the metro area and remote WA.
We need a clean, professional and high-impact full vehicle wrap design for our work vans. The vans are our mobile billboards, so the design needs to look sharp from a distance, communicate trust and competence, and clearly show what we do.
Must include:

Our company name: RT Electrical and Refrigeration
Tagline options (you can choose the strongest placement or suggest alternatives):
“Electrical | Air Conditioning | Refrigeration – Perth & Remote WA”
Licence numbers "QX417203 and MB42931"
Phone number: 0491 538 214
Website: rtelectricalrefrigeration.com.au
Email: admin@rtelectricalrefrigeration.com.au
Our existing logo (will be uploaded)

Style we want:

Professional, modern and trustworthy
Bold enough to stand out on the road but not flashy or overly busy
Clean hierarchy so the company name and phone number are readable at speed
Strong use of contrast

Colour preferences:

Prefer designs that work with our existing branding (we will upload the logo and brand colours)
Open to strong, professional colour combinations (navy/dark blue, black, white, and one accent colour such as orange, red or electric blue often work well in the trades)

Avoid:

Cluttered designs with too much text
Cartoonish or overly “tradie” looking graphics
Designs that look cheap or dated

Additional notes:

Design should scale well so we can use the same concept across multiple vans
We will need print-ready files (high-res, layered) at the end

Please upload your best concepts. We will give clear feedback and work with the winning designer to refine the final artwork for production.

Target Market(s)

commercial buildings, homes and luxury residential jobs across the metro area and remote WA.

Industry/Entity Type

Electrical, Air Conditioning and Refrigeration

Colors
0054AA
0677BA
7BADD7
CADEEF
E8F1F8

Requirements
Must have
• Our company name: RT Electrical and Refrigeration Tagline options (you can choose the strongest placement or suggest alternatives): “Electrical | Air Conditioning | Refrigeration – Perth & Remote WA” Licence numbers "QX417203 and MB42931" Phone number: 0491 538 214 Website: rtelectricalrefrigeration.com.au Email: admin@rtelectricalrefrigeration.com.au Our existing logo (will be uploaded)
Nice to have
• Professional, modern and trustworthy Bold enough to stand out on the road but not flashy or overly busy Clean hierarchy so the company name and phone number are readable at speed Strong use of contrast
Should not have
• Cluttered designs with too much text Cartoonish or overly “tradie” looking graphics Designs that look cheap or dated

```html
<!DOCTYPE html>
<html lang="en">
<head>
<meta charset="utf-8">
<title>RT Electrical and Refrigeration – Varnel Kestra Wrap</title>
<link rel="stylesheet" href="https://fonts.googleapis.com/css2?family=Montserrat:wght@600;700;800&family=Oswald:wght@400;500&display=swap">
<style>
  :root {
    --brand-blue: #0054AA;
    --wrap-blue: #1E6FD9;
    --mid-blue: #0677BA;
    --pale-blue: #CADEEF;
    --ice: #E8F1F8;
    --panel-white: #F4F4F2;
    --line: #D7DBE0;
    --page: #FFFFFF;
  }
  * { margin: 0; padding: 0; box-sizing: border-box; }
  html, body { width: 1200px; height: 1200px; overflow: hidden; background: var(--page); }
  .canvas { position: relative; width: 1200px; height: 1200px; }
  .panel { position: absolute; overflow: hidden; border: 1px solid var(--line); border-radius: 18px; }
  .panel svg.bg { position: absolute; inset: 0; }
  .heading {
    font-family: "Montserrat", sans-serif; font-weight: 800; color: var(--brand-blue);
    text-transform: uppercase; letter-spacing: 1px; line-height: 1.02;
  }
  .tag { font-family: "Oswald", sans-serif; font-weight: 500; text-transform: uppercase; letter-spacing: .5px; white-space: nowrap; }
  .abs { position: absolute; }
  .logo-box {
    position: absolute; background: var(--panel-white); display: flex; align-items: center; justify-content: center;
  }
  .logo-name { font-family: "Montserrat", sans-serif; font-weight: 800; color: var(--wrap-blue); letter-spacing: 2px; }

  /* side panel */
  .side { left: 60px; top: 110px; width: 1080px; height: 400px; background: var(--panel-white); }
  .side .logo-box { left: 48px; top: 70px; width: 230px; height: 230px; transform: rotate(-8deg); }
  .side .logo-name { font-size: 96px; }
  .side .name { left: 380px; top: 90px; width: 320px; text-align: center; font-size: 32px; color: var(--wrap-blue); }
  .side .services { left: 370px; top: 230px; width: 340px; text-align: center; font-size: 19px; color: var(--brand-blue); line-height: 1.35; }
  .side .phone { left: 722px; top: 228px; font-family: "Montserrat", sans-serif; font-weight: 700; font-size: 31px; color: var(--wrap-blue); white-space: nowrap; }
  .side .web { left: 724px; top: 278px; display: flex; align-items: center; gap: 8px; font-size: 15px; color: var(--brand-blue); }
  .side .lic { left: 948px; top: 236px; width: 122px; text-align: center; font-size: 13px; color: var(--mid-blue); line-height: 1.3; }
  .side .band-text { left: 360px; top: 350px; width: 540px; text-align: center; font-size: 16px; color: #fff; }

  /* rear panel */
  .rear { left: 90px; top: 610px; width: 500px; height: 450px; background: var(--wrap-blue); }
  .rear .logo-box { left: 28px; top: 40px; width: 120px; height: 120px; }
  .rear .logo-name { font-size: 48px; }
  .rear .name { left: 168px; top: 48px; font-size: 27px; color: var(--ice); }
  .rear .phone { left: 170px; top: 118px; font-family: "Montserrat", sans-serif; font-weight: 700; font-size: 34px; color: #fff; }
  .rear .contact { top: 198px; display: flex; align-items: center; gap: 5px; font-size: 10px; letter-spacing: 0; color: #fff; }
  .rear .web { left: 24px; }
  .rear .mail { left: 236px; }
  .rear .lic { left: 330px; top: 240px; width: 150px; text-align: center; font-size: 12px; color: #fff; line-height: 1.3; }
  .rear .strip { left: 20px; top: 370px; width: 460px; height: 34px; background: var(--panel-white); display: flex; align-items: center; justify-content: center; font-size: 14px; color: var(--brand-blue); }

  /* front panel */
  .front { left: 640px; top: 610px; width: 470px; height: 200px; background: var(--panel-white); }
  .front .logo-box { left: 48px; top: 64px; width: 80px; height: 72px; background: var(--wrap-blue); }
  .front .logo-name { font-size: 32px; color: var(--panel-white); }
  .front .name { left: 146px; top: 74px; font-size: 22px; color: var(--wrap-blue); }

  .dot { width: 14px; height: 14px; border-radius: 50%; background: currentColor; display: inline-block; flex: none; opacity: .85; }
</style>
</head>
<body>
<main class="canvas">

  <section class="panel side" aria-label="Side wrap panel">
    <svg class="bg" width="1080" height="400" viewBox="0 0 1080 400" aria-hidden="true">
      <polygon points="0,0 290,0 330,400 0,400" fill="var(--wrap-blue)"/>
      <rect x="330" y="330" width="560" height="56" fill="var(--wrap-blue)"/>
    </svg>
    <div class="logo-box"><span class="logo-name">RT</span></div>
    <h1 class="abs heading name">Electrical &amp; Refrigeration</h1>
    <p class="abs tag services">Electrical | Air Conditioning<br>Refrigeration – Perth &amp; Remote WA</p>
    <p class="abs phone">0491 538 214</p>
    <p class="abs tag web"><span class="dot"></span>rtelectricalrefrigeration.com.au</p>
    <p class="abs tag lic">LIC#<br>QX417203 &amp; MB42931</p>
    <p class="abs tag band-text">You can choose the strongest placement or suggest alternatives</p>
  </section>

  <section class="panel rear" aria-label="Rear wrap panel">
    <div class="logo-box"><span class="logo-name">RT</span></div>
    <h2 class="abs heading name">Electrical &amp;<br>Refrigeration</h2>
    <p class="abs phone">0491 538 214</p>
    <p class="abs tag contact web"><span class="dot"></span>rtelectricalrefrigeration.com.au</p>
    <p class="abs tag contact mail"><span class="dot"></span>admin@rtelectricalrefrigeration.com.au</p>
    <p class="abs tag lic">LIC#<br>QX417203 &amp; MB42931</p>
    <p class="abs tag strip">Electrical | Air Conditioning | Refrigeration – Perth &amp; Remote WA</p>
  </section>

  <section class="panel front" aria-label="Front wrap panel">
    <div class="logo-box"><span class="logo-name">RT</span></div>
    <h2 class="abs heading name">Electrical &amp;<br>Refrigeration</h2>
  </section>

</main>
</body>
</html>
```